" Trabalho há 10 anos juntamente com meu esposo, também arquiteto. Ambos com atuação em segmento de educação e meu esposo na prefeitura. Estamos oficializando o escritório a partir de agora. Atuamos nas diversas áreas de projeto de arquitetura de edificações de vários portes (casas, prédios), urbanismo (praças, parques, loteamentos) , interiores e consultoria na aprovação de projetos de diversas naturezas. "

```html
<!DOCTYPE html>
<html lang="pt-BR">
<head>
<meta charset="UTF-8">
<title>Traço Aberto — Cartão de Visita</title>
<link rel="stylesheet" href="https://fonts.googleapis.com/css2?family=Raleway:wght@300;400&family=Open+Sans:wght@400;600&display=swap">
<style>
  :root {
    --page-bg: #ececea;
    --card-dark: #5b5b5d;
    --card-light: #ffffff;
    --ink-dark: #3c3c3e;
    --ink-light: #e6e6e6;
    --mark-faint: #d9d9d9;
    --band: #4e4e50;
  }
  * { margin: 0; padding: 0; box-sizing: border-box; }
  html, body {
    width: 1200px; height: 1200px; overflow: hidden;
    background: var(--page-bg);
  }
  .canvas {
    width: 1200px; height: 1200px;
    display: flex; flex-direction: column;
    align-items: center; justify-content: center;
    gap: 70px;
  }
  .card {
    width: 770px; height: 440px;
    position: relative;
    box-shadow: 0 6px 22px rgba(0,0,0,0.18);
    overflow: hidden;
  }

  /* Front */
  .card--front {
    background: var(--card-dark);
    display: flex; flex-direction: column;
    align-items: center; justify-content: center;
  }
  .brand-dot {
    width: 70px; height: 70px;
    border: 2px solid var(--ink-light);
    border-radius: 50%;
    margin-bottom: 26px;
  }
  .brand-name {
    font-family: "Raleway", sans-serif;
    font-weight: 300;
    font-size: 46px;
    letter-spacing: 3px;
    color: var(--ink-light);
    text-transform: uppercase;
    line-height: 1;
  }
  .brand-tagline {
    font-family: "Raleway", sans-serif;
    font-weight: 300;
    font-size: 15px;
    letter-spacing: 6px;
    color: var(--ink-light);
    text-transform: uppercase;
    margin-top: 12px;
  }

  /* Back */
  .card--back { background: var(--card-light); }
  .side-band {
    position: absolute; top: 0; right: 0;
    width: 24px; height: 100%;
    background: var(--band);
  }
  .faint-mark {
    position: absolute; left: 40px; top: 60px;
    width: 330px; height: 330px;
    border: 6px solid var(--mark-faint);
    border-radius: 50%;
    display: flex; align-items: center; justify-content: center;
  }
  .faint-mark span {
    font-family: "Raleway", sans-serif;
    font-weight: 300;
    font-size: 38px;
    letter-spacing: 2px;
    text-transform: uppercase;
    color: var(--mark-faint);
  }
  .contact {
    position: absolute; right: 58px; top: 52px;
    text-align: right;
    font-family: "Open Sans", sans-serif;
    color: var(--ink-dark);
  }
  .person-name { font-size: 28px; font-weight: 400; line-height: 1.15; }
  .person-role { font-size: 28px; font-weight: 400; line-height: 1.15; margin-bottom: 40px; }
  .contact-line {
    display: flex; justify-content: flex-end; align-items: center;
    gap: 10px;
    font-size: 19px;
    margin-bottom: 14px;
  }
  .contact-line svg { width: 22px; height: 22px; fill: var(--ink-dark); flex: none; }
  .contact-line--address { align-items: flex-start; }
  .address { line-height: 1.15; }
</style>
</head>
<body>
<main class="canvas">
  <section class="card card--front" aria-label="Frente do cartão">
    <div class="brand-dot" aria-hidden="true"></div>
    <h1 class="brand-name">Traço Aberto</h1>
    <p class="brand-tagline">Arquitetura e Urbanismo</p>
  </section>

  <section class="card card--back" aria-label="Verso do cartão">
    <div class="faint-mark" aria-hidden="true"><span>Traço Aberto</span></div>
    <div class="contact">
      <p class="person-name">Nome sobrenome</p>
      <p class="person-role">função</p>
      <p class="contact-line">contato@contato.com
        <svg viewBox="0 0 24 24" aria-hidden="true"><path d="M2 5h20v14H2z M3.5 6.5 12 13l8.5-6.5v-.2h-17z" fill-rule="evenodd"/></svg>
      </p>
      <p class="contact-line">(00)0000-0000
        <svg viewBox="0 0 24 24" aria-hidden="true"><path d="M6.6 10.8a15 15 0 0 0 6.6 6.6l2.2-2.2c.3-.3.7-.4 1-.2 1.1.4 2.3.6 3.6.6.6 0 1 .4 1 1V20c0 .6-.4 1-1 1A17 17 0 0 1 3 4c0-.6.4-1 1-1h3.5c.6 0 1 .4 1 1 0 1.3.2 2.5.6 3.6.1.3 0 .7-.2 1z"/></svg>
      </p>
      <p class="contact-line">(00)0000-0000
        <svg viewBox="0 0 24 24" aria-hidden="true"><path d="M7 1h10a2 2 0 0 1 2 2v18a2 2 0 0 1-2 2H7a2 2 0 0 1-2-2V3a2 2 0 0 1 2-2zm0 3v14h10V4zm5 15.2a1.2 1.2 0 1 0 0 2.4 1.2 1.2 0 0 0 0-2.4z" fill-rule="evenodd"/></svg>
      </p>
      <div class="contact-line contact-line--address">
        <p class="address">rua sem nome,00<br>Bairro Sem Nome<br>Cidade Sem Nome</p>
        <svg viewBox="0 0 24 24" aria-hidden="true"><path d="M12 2a7 7 0 0 0-7 7c0 5.2 7 13 7 13s7-7.8 7-13a7 7 0 0 0-7-7zm0 9.5a2.5 2.5 0 1 1 0-5 2.5 2.5 0 0 1 0 5z"/></svg>
      </div>
    </div>
    <div class="side-band" aria-hidden="true"></div>
  </section>
</main>
</body>
</html>
```